Web Design

Looking for web designer for total service. We would like to make it in English and Japanese for now. Also need to make Tablet version. Our website is www.brindlecove.com and www.quartzmeadow .com

```html
<!DOCTYPE html>
<html lang="en">
<head>
<meta charset="utf-8">
<title>Quartz Meadow</title>
<link href="https://fonts.googleapis.com/css2?family=Roboto:wght@300;400;500&family=Open+Sans:wght@400&display=swap" rel="stylesheet">
<style>
:root{
  --green:#2a7a14;
  --brown:#2e1c15;
  --orange:#e2562a;
  --white:#ffffff;
  --ink:#222222;
  --muted:#555555;
  --footer:#ece9df;
  --footer-low:#f1efea;
  --rule:#cfcbc0;
}
*{box-sizing:border-box;margin:0;padding:0}
html,body{width:1200px;height:2323px;overflow:hidden;background:var(--white)}
body{position:relative;font-family:"Roboto",sans-serif;color:var(--ink)}
.abs{position:absolute}
h1,h2,h3,h4{font-weight:400}

/* header */
.site-header{left:0;top:0;width:1200px;height:119px;background:var(--white)}
.brand{left:183px;top:34px;display:flex;align-items:center;gap:10px;font-size:26px;font-weight:500;color:var(--green)}
.brand-dot{width:22px;height:22px;border-radius:50%;background:var(--green)}
.lang{left:899px;top:56px;width:113px;height:34px;border:1px solid #ddd;border-radius:3px;display:flex;align-items:center;justify-content:center;gap:8px;font-size:13px;color:#333}
.lang-flag{width:26px;height:16px;background:#2b3d8a}
.lang-caret{width:0;height:0;border-left:4px solid transparent;border-right:4px solid transparent;border-top:5px solid #333}

/* nav */
.main-nav{left:0;top:119px;width:1200px;height:51px;background:var(--brown)}
.nav-item{top:0;height:51px;line-height:51px;font-size:16.5px;font-weight:500;color:var(--white);white-space:nowrap}
.nav-item.active{background:var(--green);width:97px;text-align:center}

/* hero */
.hero{left:0;top:170px;width:1200px;height:581px;overflow:hidden;background:linear-gradient(100deg,#6b5238 0%,#4a4540 30%,#333a47 55%,#2d3340 100%)}
.hero-curve{left:0;top:0}
.hero-title{left:0;top:320px;width:1200px;text-align:center;font-size:42px;color:var(--white)}
.hero-sub{left:0;top:380px;width:1200px;text-align:center;font-size:19.5px;font-weight:300;line-height:25px;color:var(--white)}
.btn{display:flex;align-items:center;justify-content:center;border-radius:24px;font-weight:500}
.hero-btn{left:522px;top:449px;width:158px;height:47px;background:var(--orange);color:var(--white);font-size:17px}
.slider-dots{left:553px;top:617px;display:flex;align-items:center;gap:5px}
.dot{width:7px;height:7px;border-radius:50%;background:#9aa0a8}
.dot.on{background:var(--white)}
.arrow{width:14px;height:14px;border-radius:50%;background:var(--white)}

/* cards */
.card{top:734px;width:259px;height:291px;border-radius:9px;color:var(--white);text-align:center}
.card.green{background:var(--green)}
.card.brown{background:var(--brown)}
.card-icon{position:absolute;left:99px;top:26px}
.card-title{position:absolute;left:0;top:103px;width:100%;font-size:20px}
.card-text{position:absolute;left:30px;top:139px;width:199px;font-size:13.5px;line-height:17.5px}
.card-btn{position:absolute;left:67px;top:232px;width:124px;height:39px;background:var(--white);color:var(--ink);font-size:14px}

/* news */
.news{left:0;top:1087px;width:1200px;height:402px;background:linear-gradient(90deg,#3d2a20 0%,#5a3f2c 40%,#6b4b33 65%,#4c3526 100%)}
.news-label{left:0;top:1147px;width:1200px;text-align:center;font-size:19.5px;color:var(--white)}
.news-title{left:0;top:1169px;width:1200px;text-align:center;font-size:35px;font-weight:400;color:var(--white)}
.news-sub{left:0;top:1222px;width:1200px;text-align:center;font-size:19.5px;color:var(--white)}
.news-text{left:300px;top:1261px;width:600px;text-align:center;font-size:17.5px;font-weight:300;line-height:28px;color:var(--white)}
.news-btn{left:517px;top:1367px;width:159px;height:46px;background:var(--green);color:var(--white);font-size:17px}

/* souvenir */
.souvenir-title{left:203px;top:1562px;width:420px;font-size:28px;line-height:36px;color:var(--ink)}
.souvenir-text{left:209px;top:1689px;width:440px;font-family:"Open Sans",sans-serif;font-size:12.8px;line-height:23px;color:var(--muted)}
.product{border-radius:4px}

/* footer */
.site-footer{left:0;top:2015px;width:1200px;height:234px;background:var(--footer);border-top:3px solid var(--rule)}
.footer-col{top:2080px;font-size:14.5px;line-height:26.5px;color:#333}
.footer-col h4{font-size:15.5px;color:var(--ink);margin-bottom:1px}
.socials{display:flex;gap:6px;margin-top:4px}
.social{width:32px;height:32px;border-radius:50%;border:1.5px solid var(--ink)}
.copyright{left:0;top:2249px;width:1200px;height:74px;background:var(--footer-low);border-top:1px solid var(--rule);text-align:center;line-height:60px;font-size:13px;color:#666}
</style>
</head>
<body>

<header class="site-header abs">
  <div class="brand abs"><span class="brand-dot"></span>Quartz Meadow</div>
  <div class="lang abs"><span class="lang-flag"></span>English<span class="lang-caret"></span></div>
</header>

<nav class="main-nav abs">
  <span class="nav-item active abs" style="left:183px">HOME</span>
  <span class="nav-item abs" style="left:300px">OUR PRODUCTS</span>
  <span class="nav-item abs" style="left:460px">ABOUT US</span>
  <span class="nav-item abs" style="left:562px">ONLINE SHOPPING</span>
  <span class="nav-item abs" style="left:729px">INQUIRIES</span>
  <span class="nav-item abs" style="left:831px">RECRUIT</span>
  <span class="nav-item abs" style="left:921px">CONTACT</span>
</nav>

<section class="hero abs" role="img" aria-label="Bowl of peanut butter with scattered peanuts on a dark wooden table">
  <svg class="hero-curve abs" width="1200" height="581" viewBox="0 0 1200 581">
    <path d="M0 581 L0 581 Q600 380 1200 573 L1200 581 Z" fill="#ffffff"/>
  </svg>
</section>
<h1 class="hero-title abs">Rely on Businees Expertin Hawaii</h1>
<p class="hero-sub abs">We also do marketing consulting for customers who want to<br>sell their products in Hawaii or the mainland USA.</p>
<a class="btn hero-btn abs">Read More</a>
<div class="slider-dots abs">
  <span class="arrow"></span><span class="dot on"></span><span class="dot"></span><span class="dot"></span><span class="dot"></span><span class="arrow"></span>
</div>

<div class="card green abs" style="left:183px">
  <svg class="card-icon" width="60" height="62" viewBox="0 0 60 62" fill="none" stroke="#fff" stroke-width="2.5">
    <rect x="10" y="4" width="40" height="10" rx="2"/><rect x="5" y="14" width="50" height="44" rx="6"/>
    <rect x="12" y="24" width="36" height="22" rx="4"/><circle cx="21" cy="35" r="4"/><circle cx="33" cy="31" r="3"/><circle cx="38" cy="40" r="3"/>
  </svg>
  <h3 class="card-title">What we do</h3>
  <p class="card-text">Aonsectetuer mi a ultricies massa est sed nisl Class aptent taciti sociosqu ad litora torquent per conubia</p>
  <a class="btn card-btn">Read More</a>
</div>
<div class="card brown abs" style="left:460px">
  <svg class="card-icon" width="62" height="62" viewBox="0 0 62 62" fill="none" stroke="#fff" stroke-width="2.5">
    <path d="M31 4a27 27 0 1 1-16 49L5 58l4-11A27 27 0 0 1 31 4z"/>
    <circle cx="31" cy="18" r="3" fill="#fff"/><path d="M27 26h5v18M26 44h11"/>
  </svg>
  <h3 class="card-title">About Us</h3>
  <p class="card-text">Aonsectetuer mi a ultricies massa est sed nisl Class aptent taciti sociosqu ad litora torquent per conubia</p>
  <a class="btn card-btn">Read More</a>
</div>
<div class="card green abs" style="left:743px">
  <svg class="card-icon" width="62" height="62" viewBox="0 0 62 62" fill="none" stroke="#fff" stroke-width="2.5">
    <circle cx="31" cy="22" r="17"/><circle cx="31" cy="18" r="6"/><path d="M22 33c2-6 16-6 18 0"/>
    <circle cx="14" cy="44" r="5"/><circle cx="48" cy="44" r="5"/><path d="M4 60c1-8 19-8 20 0M38 60c1-8 19-8 20 0"/>
  </svg>
  <h3 class="card-title">Recruit</h3>
  <p class="card-text">Aonsectetuer mi a ultricies massa est sed nisl Class aptent taciti sociosqu ad litora torquent per conubia</p>
  <a class="btn card-btn">Read More</a>
</div>

<section class="news abs" role="img" aria-label="Stack of pancakes topped with blueberries and syrup"></section>
<p class="news-label abs">Information</p>
<h2 class="news-title abs">What's New</h2>
<p class="news-sub abs">Integer congue augue et malesuada iaculis ipsum</p>
<p class="news-text abs">porttitor mattis enim In massa libero interdum nec interdum vel blandit sed nulla In ullamcorper est eget tempor cursus neque mi consectetuer mi a ultricies massa est sed nisl Class aptent taciti sociosqu</p>
<a class="btn news-btn abs">Read More</a>

<h2 class="souvenir-title abs">The souvenir you want is sure to be found Made in Hawaii's Gourmet item</h2>
<p class="souvenir-text abs">"Brindle Cove" where premium gourmet items developed by Japanese staff to match the Japanese taste are repeated while repeating trial and error with local companies in Hawaii. Researching high-quality souvenirs and making unique "Made in Hawaii" goods that shape "I hope there is such a product" is popular among souvenirs. We devised measures to make it easy to carry packages, and also recommended for bulk purchase such as balamaki souvenirs. The popular pancake mix only dissolves in water, and finished fluffy pancake. There is also a mini size mix set so you can enjoy various flavors. Products are on sale at Pali Market, Lanai Mart and other convenience stores.</p>
<div class="product abs" style="left:683px;top:1559px;width:159px;height:144px;background:linear-gradient(180deg,#e9e7e2,#cfcac0)" role="img" aria-label="Jars of coconut oil"></div>
<div class="product abs" style="left:683px;top:1721px;width:159px;height:157px;background:linear-gradient(180deg,#e7c9c2,#b8583c)" role="img" aria-label="Boxes of gourmet pancake mix"></div>
<div class="product abs" style="left:865px;top:1591px;width:160px;height:158px;background:linear-gradient(180deg,#e8b86a,#c98a2a)" role="img" aria-label="Bear-shaped bottles of honey"></div>
<div class="product abs" style="left:865px;top:1774px;width:160px;height:158px;background:linear-gradient(180deg,#d8d2c4,#6b3d22)" role="img" aria-label="Three jars of peanut butter"></div>

<footer class="site-footer abs"></footer>
<div class="footer-col abs" style="left:183px"><h4>ADDRESS</h4>415 Makana Lane 12,<br>Kailua HI 96734</div>
<div class="footer-col abs" style="left:392px"><h4>OFFICE HOURS</h4>Mon - Fri: 8: 00 am - 4: 45 pm</div>
<div class="footer-col abs" style="left:663px"><h4>CONTACT</h4>Tel: (808) 555 - 0142<br>Fax: (808) 555-0178<br>email:info@quartzmeadow.com</div>
<div class="footer-col abs" style="left:906px"><h4>FOLLOW US</h4><div class="socials"><span class="social"></span><span class="social"></span><span class="social"></span></div></div>
<div class="copyright abs">© 2018 Company Name  All right reserved</div>

</body>
</html>
```